Business Card Design Project

Hello,

We have just created our new COMPANY LOGO via Pixel Harbor and would not like to turn our attention to new Business Cards.

We are a printing company based in Singapore & Las Vegas. We specialize in blue-print printing for the Architectural, Engineering and Construction industries

The design should be simple, professional, clean and organized.

The Business Cards should "pop" when seen and will hopefully be something that makes you look twice.

We have two different Pan-tones that we use for our company, feel free to use them if you think they will work for your design?

Orange: PMS 021
Gray: PMS 431

I have attached our current logo for your use and reference which should obvious be on our business cards.

Considering we have two locations on different continents, we need business cards templates where the address details need to be interchangeable for each different location (total 2)

First one:
38 Merrow Lane #03-11 to #03-15
Singapore 528473
Tel : +65 6847-3920
Fax : +65 6843-7702

Second one:
2381 W. Tanfield Rd, Suite 204
Las Vegas, Nevada 89152
Tel : (702) 555-4137
Fax : (702) 555-4189

We would also like to list a few of our key services on the card. Here are a few examples to get you going.

Plan Printing & Plotting
Digital Colour Printing
Cadline Printing
Specialty Book Making
Scanning & Archiving
Collection & Delivey

This is the first time i have requested for business cards to be created so please let me know if you require any additional information.
Many Thanks,
Tobin
Updates

Project Deadline Extended
Reason: It took us longer than expected to finalize our Company Logo We look forward to receiving your designs.

Target Market(s)

Our Target Market is construction related people.
Construction
Architecture
Engineering

Industry/Entity Type

Printing

Font styles to use
Other font styles liked:
• Times New Roman

Colors
faa54b
ffffff

Requirements
Must have
• The business card must have our Company Logo (attached)
The font used must be Times New Roman
Should not have
• Playful images of print designs and/or logos

```html
<!DOCTYPE html>
<html lang="en">
<head>
<meta charset="utf-8">
<title>Merrow Print Works – Business Card</title>
<link rel="stylesheet" href="https://fonts.googleapis.com/css2?family=Tinos:ital,wght@0,400;0,700;1,700&display=swap">
<style>
  :root {
    --brand-orange: #f47a0c;
    --card-black: #0a0a0e;
    --card-white: #ffffff;
    --ink: #111111;
    --bg-light: #6479f7;
    --bg-mid: #2b3470;
    --bg-dark: #02030a;
    --edge: #8a8c96;
  }
  * { margin: 0; padding: 0; box-sizing: border-box; }
  html, body { width: 1200px; height: 1000px; overflow: hidden; }
  body {
    font-family: "Tinos", "Times New Roman", serif;
    background: radial-gradient(circle at 150px 280px, var(--bg-light) 0%, #4a5bcf 22%, var(--bg-mid) 55%, #141a3a 78%, var(--bg-dark) 100%);
    position: relative;
  }
  .card {
    position: absolute;
    left: 290px;
    width: 619px;
    height: 359px;
    border-radius: 16px;
    box-shadow: -8px 8px 8px rgba(0,0,0,0.55);
    text-align: center;
    overflow: hidden;
  }
  .card--front {
    top: 128px;
    background: var(--card-black);
    border: 1px solid var(--edge);
  }
  .card--back {
    top: 514px;
    height: 357px;
    background: var(--card-white);
    border: 1px solid #cfd0d6;
    color: var(--ink);
  }
  .brand-name {
    position: absolute;
    left: 0; right: 0;
    color: var(--brand-orange);
    font-weight: 700;
    letter-spacing: 0.5px;
  }
  .card--front .brand-name { top: 196px; font-size: 34px; }
  .card--back .brand-name { top: 82px; font-size: 30px; }
  .front-tagline {
    position: absolute;
    left: 0; right: 0; top: 312px;
    color: #ffffff;
    font-size: 19px;
    font-weight: 700;
    font-style: italic;
  }
  .contact {
    position: absolute;
    left: 0; right: 0; top: 168px;
    font-size: 17px;
    line-height: 22px;
  }
  .contact .gap { display: inline-block; width: 14px; }
  .divider {
    position: absolute;
    left: 0; right: 0; top: 254px;
    height: 2px;
    background: var(--ink);
  }
  .services-title {
    position: absolute;
    left: 0; right: 0; top: 267px;
    font-size: 17px;
  }
  .services {
    position: absolute;
    left: 22px; top: 295px;
    width: 580px;
    list-style: none;
    display: grid;
    grid-template-columns: 198px 190px 192px;
    row-gap: 2px;
    font-size: 17px;
    line-height: 20px;
    text-align: left;
    white-space: nowrap;
  }
  .services li::before {
    content: "";
    display: inline-block;
    width: 7px; height: 7px;
    margin-right: 2px;
    border-radius: 50%;
    background: var(--brand-orange);
    vertical-align: 2px;
  }
</style>
</head>
<body>
  <section class="card card--front">
    <div class="brand-name">Merrow Print Works</div>
    <p class="front-tagline">A Member of the MPW Group of Companies</p>
  </section>

  <section class="card card--back">
    <div class="brand-name">Merrow Print Works</div>
    <address class="contact" style="font-style: normal;">
      38 Merrow Lane #03-11 to #03-15, Singapore 528473<br>
      Tel : +65 6847-3920<span class="gap"></span>Fax : +65 6843-7702
    </address>
    <div class="divider"></div>
    <h2 class="services-title" style="font-weight: 400;">Our Key Services</h2>
    <ul class="services">
      <li>Plan Printing &amp; Plotting</li>
      <li>Digital Colour Printing</li>
      <li>Cadline Printing</li>
      <li>Specialty Book Making</li>
      <li>Scanning &amp; Archiving</li>
      <li>Collection &amp; Delivery</li>
    </ul>
  </section>
</body>
</html>
```